Lumen Beauty & Spa Business Card Design

Hello, I have a Beauty salon On my own Property. It is a Balinese Style Salon with a Spa & Sauna together with all beauty Options available. I have strived myself to get trained In Indonesia as well as here so I can offer my clients something "unique & special" somewhere to unwind as well as be pampered and step out of reality for even a little while.

So with all this in mind I would like to keep everything on the "natural style look" if possible....

I was hoping to have some kind Of Kraft look paper or background look, with a Olive/lime Natural Green colour Logo and Name on the front. "Lumen Beauty & Spa"

Details (im really not sure on how it should be placed on the card whether back or front?)
I'd really like written somewhere on the card, somewhere
.... Lumen Daydream ...

also if room maybe a few things that I do eg. Waxing, Tanning, teeth Whitening, all kinds of Beauty and much more.

DETAILS are
Lumen Beauty & Spa
Marisa Pellow
Ph: 04 873 21 560
Address: 12 Tarrow Court
Fernwick NSW 2391

(facebook logo) www.facenook.example/LumenBeautySpa

I think this is all the info that I need on the card.. if I have forgotten anything or if you need anything else please dont hesitate to contact me....
& just maybe a few dotted lines so I can write appt times etc.. I was also thinking maybe a QR BarCode. Sorry this is the first time I have done any business cards so forgive me I dont really have a clue.

please let me know what else you need me to do from here thanks for your time.
Risa

Industry/Entity Type

Salon

Font styles to use
Script

Colors
acd036
9bcb3c

```html
<!DOCTYPE html>
<html lang="en">
<head>
<meta charset="utf-8">
<title>Lumen Beauty &amp; Spa – Business Card</title>
<link rel="stylesheet" href="https://fonts.googleapis.com/css2?family=Exo+2:wght@400;500&family=Great+Vibes&display=swap">
<style>
  :root {
    --lime: #acd036;
    --lime-deep: #9bcb3c;
    --kraft-light: #e6d5b5;
    --kraft-mid: #d8c29a;
    --kraft-grain: rgba(120, 90, 50, 0.05);
    --backdrop: #d8d9d6;
    --ink-light: #ffffff;
    --ink-soft: #7a6a4e;
  }
  html, body {
    margin: 0;
    width: 1200px;
    height: 899px;
    overflow: hidden;
    background: var(--backdrop);
    font-family: "Exo 2", sans-serif;
  }
  .card {
    position: absolute;
    left: 150px;
    top: 192px;
    width: 900px;
    height: 514px;
    border-radius: 44px;
    overflow: hidden;
    background:
      repeating-linear-gradient(87deg, var(--kraft-grain) 0 2px, transparent 2px 5px),
      repeating-linear-gradient(-12deg, var(--kraft-grain) 0 1px, transparent 1px 7px),
      linear-gradient(120deg, var(--kraft-light) 0%, var(--kraft-mid) 70%);
    box-shadow: 0 14px 40px rgba(0,0,0,0.18);
  }
  .card__shapes { position: absolute; inset: 0; }

  .brand {
    position: absolute;
    left: 56px;
    top: 130px;
    display: flex;
    align-items: center;
    gap: 16px;
  }
  .brand__figure {
    width: 96px;
    height: 200px;
    border-radius: 48px 48px 40px 40px;
    background: radial-gradient(ellipse at 50% 40%, var(--lime) 0%, rgba(172,208,54,0.35) 70%, rgba(172,208,54,0) 100%);
  }
  .brand__text { width: 200px; }
  .brand__name {
    margin: 0;
    color: var(--lime-deep);
    font-weight: 500;
    font-size: 21px;
    line-height: 26px;
    letter-spacing: 0.5px;
  }
  .brand__tagline {
    margin: 6px 0 0;
    color: var(--lime-deep);
    font-family: "Great Vibes", cursive;
    font-size: 30px;
    line-height: 34px;
  }
  .brand__services {
    margin: 8px 0 0;
    color: var(--ink-soft);
    font-size: 12px;
    line-height: 17px;
    letter-spacing: 0.3px;
  }

  .contact {
    position: absolute;
    right: 42px;
    top: 0;
    width: 330px;
    text-align: right;
    color: var(--ink-light);
  }
  .contact__name {
    margin: 100px 0 0;
    font-size: 29px;
    font-weight: 500;
    letter-spacing: 2px;
  }
  .contact__role {
    margin: 4px 0 0;
    font-size: 18px;
    letter-spacing: 0.6px;
  }
  .contact__address {
    margin: 32px 0 0;
    font-size: 21px;
    line-height: 32px;
    letter-spacing: 0.8px;
  }
  .contact__lines {
    list-style: none;
    margin: 20px 0 0;
    padding: 0;
    font-size: 17px;
    letter-spacing: 0.5px;
  }
  .contact__lines li {
    display: flex;
    justify-content: flex-end;
    align-items: center;
    gap: 12px;
    height: 32px;
  }
  .contact__lines li.is-small { font-size: 14px; letter-spacing: 0.2px; }
  .icon { width: 18px; height: 18px; flex: none; }

  .appointment {
    margin: 16px 0 0;
    font-size: 14px;
    letter-spacing: 0.5px;
  }
  .appointment__row {
    display: flex;
    justify-content: flex-end;
    align-items: flex-end;
    gap: 10px;
    height: 28px;
  }
  .appointment__line {
    width: 210px;
    border-bottom: 2px dotted var(--ink-light);
  }
</style>
</head>
<body>
  <div class="card">
    <svg class="card__shapes" width="900" height="514" viewBox="0 0 900 514" aria-hidden="true">
      <path d="M440 0 C420 250 360 420 228 514 L900 514 L900 0 Z" fill="var(--lime)"/>
      <path d="M458 0 C440 250 380 428 256 514" fill="none" stroke="#ffffff" stroke-width="4"/>
    </svg>

    <div class="brand">
      <div class="brand__figure" role="img" aria-label="Lime green line illustration of a woman's silhouette with leaves, the spa emblem"></div>
      <div class="brand__text">
        <p class="brand__name">Lumen<br>Beauty &amp; Spa</p>
        <p class="brand__tagline">Lumen Daydream</p>
        <p class="brand__services">Waxing · Tanning<br>Teeth Whitening<br>All kinds of Beauty &amp; more</p>
      </div>
    </div>

    <div class="contact">
      <p class="contact__name">MARISA PELLOW</p>
      <p class="contact__role">Beauty Therapist</p>
      <p class="contact__address">12 Tarrow Court<br>Fernwick NSW 2391</p>
      <ul class="contact__lines">
        <li>04 873 21 560
          <svg class="icon" viewBox="0 0 24 24"><path d="M6 2l4 4-2 3c1 3 4 6 7 7l3-2 4 4-3 4C10 22 2 14 2 5z" fill="#fff"/></svg>
        </li>
        <li class="is-small">www.facenook.example/LumenBeautySpa
          <svg class="icon" viewBox="0 0 24 24"><circle cx="12" cy="12" r="9" fill="#fff"/></svg>
        </li>
      </ul>
      <div class="appointment">
        <div class="appointment__row"><span>Appt date</span><span class="appointment__line"></span></div>
        <div class="appointment__row"><span>Time</span><span class="appointment__line"></span></div>
      </div>
    </div>
  </div>
</body>
</html>
```